BRIM Outreach Partners Business Card Rebrand

Hello Designers! We are looking for help designing our new business card to go in conjunction with our company rebrand. Unfortunately, we have an event mid June that requires we get these printed ASAP (before our new website is launched.) We have a mostly complete Brand Book which I have uploaded to this request for your reference to company information, style, fonts. I've also enclosed our logo file in .eps & .jpg. Attached is a sample business card my boss liked but said was "too simple." I made it in Canva and do not profess to be a designer. NOT FOR DESIGN REFERENCE, ONLY FOR CONTEXT Here is what our old website looks like: https://brimoutreachpartners.com/.

```html
<!DOCTYPE html>
<html lang="en">
<head>
<meta charset="utf-8">
<title>BRIM Outreach Partners – Business Card</title>
<link rel="stylesheet" href="https://fonts.googleapis.com/css2?family=Montserrat:wght@700&family=Open+Sans:wght@400;700&display=swap">
<style>
  :root {
    --stage: #232323;
    --card: #141414;
    --card-back: #1b1b1b;
    --accent: #4fb3e6;
    --ink: #ffffff;
    --muted: #e6e6e6;
  }
  * { box-sizing: border-box; margin: 0; padding: 0; }
  html, body { width: 1200px; height: 780px; overflow: hidden; background: var(--stage); }
  .canvas { position: relative; width: 1200px; height: 780px; background: var(--stage); }

  .card {
    position: absolute;
    width: 540px; height: 308px;
    border-radius: 22px;
    border: 3px solid var(--accent);
    overflow: hidden;
    box-shadow: 0 14px 30px rgba(0,0,0,.45);
  }

  /* Back side */
  .card-back { left: 70px; top: 70px; background: var(--card-back); }
  .card-back .pattern-area {
    position: absolute; inset: 0;
    background: radial-gradient(circle at 55% 40%, #262626 0%, #191919 60%, #121212 100%);
  }
  .card-back .back-wordmark {
    position: absolute; left: 0; right: 0; top: 50%;
    transform: translateY(-50%);
    text-align: center;
    font-family: 'Montserrat', sans-serif; font-weight: 700;
    font-size: 18px; color: var(--accent); letter-spacing: .5px;
  }

  /* Front side */
  .card-front { left: 590px; top: 400px; background: var(--card); }
  .front-wordmark {
    position: absolute; left: 34px; top: 34px;
    font-family: 'Montserrat', sans-serif; font-weight: 700;
    font-size: 26px; line-height: 1.05; color: var(--ink);
  }
  .feature-disc { position: absolute; left: 318px; top: 26px; width: 200px; height: 200px; }
  .identity { position: absolute; left: 34px; top: 150px; padding-left: 14px; }
  .identity::before {
    content: ""; position: absolute; left: -34px; top: 4px;
    width: 38px; height: 36px; background: var(--accent);
  }
  .person-name {
    font-family: 'Open Sans', sans-serif; font-weight: 700;
    font-size: 19px; color: var(--accent); letter-spacing: .3px;
  }
  .person-role {
    font-family: 'Open Sans', sans-serif; font-weight: 400;
    font-size: 12px; color: var(--muted); letter-spacing: .4px;
  }
  .contact-list {
    position: absolute; left: 48px; top: 216px; list-style: none;
    font-family: 'Open Sans', sans-serif; font-weight: 400;
    font-size: 12px; line-height: 1.45; color: var(--muted);
  }
</style>
</head>
<body>
<main class="canvas">

  <section class="card card-back" aria-label="Card back">
    <div class="pattern-area" role="img" aria-label="Repeating tone-on-tone brand pattern"></div>
    <p class="back-wordmark">BRIM Outreach Partners</p>
  </section>

  <section class="card card-front" aria-label="Card front">
    <p class="front-wordmark">BRIM Outreach<br>Partners</p>
    <svg class="feature-disc" viewBox="0 0 200 200" aria-hidden="true">
      <circle cx="100" cy="100" r="100" fill="var(--accent)"/>
    </svg>
    <div class="identity">
      <p class="person-name">DANA WHITFORD-LANE</p>
      <p class="person-role">MANAGING PARTNER</p>
    </div>
    <ul class="contact-list">
      <li>+945-555-0142</li>
      <li>Denver, CO based (Mountain Time)</li>
      <li>dana@brimoutreachpartners.com</li>
      <li>www.brimoutreachpartners.com</li>
    </ul>
  </section>

</main>
</body>
</html>
```